New Meal Prep Flyer for New Package Deals

We are looking for a design that displays our new packages that we offer. If you take a look at our website www.brambleforkmeals.com, and click on packages , you'll see the way we display them currently . We would like something similar to that in style . The first package is called "Horizon" and this package will be a 1 week package (7 days ), 2 meals a day, for a price of $195.00. The second package is called "Amber" and this package will be a 3 week package (21 days) 2 meals per day, for a price of $546.00 , the third package is a 6 week+ package (45 days), and it is called "Evergreen" , 2 meals per day , and the price is $1080.00 .
For the Amber Package , can you put next to it "Save $42.00!"
For the Evergreen Package, can you put next to it "Save $180!"
We also want our logo on the flyer (see attached), and we are just looking for a 1 page flyer , 8 1/2 x 11.

```html
<!DOCTYPE html>
<html lang="en">
<head>
<meta charset="utf-8">
<title>Bramblefork Meal Prep Packages</title>
<link href="https://fonts.googleapis.com/css2?family=Roboto:wght@400;500;700;900&family=Open+Sans:wght@400;600&display=swap" rel="stylesheet">
<style>
  :root {
    --backdrop: #7f7f7f;
    --navy: #2b3c62;
    --navy-deep: #243454;
    --green: #8dc63f;
    --green-dark: #63ad3a;
    --grey-top: #8f8f8f;
    --grey-bottom: #c4c4c4;
    --orange-top: #e2621f;
    --orange-bottom: #f4b01f;
    --white: #ffffff;
    --price-grey: #8a8a8a;
  }
  * { margin: 0; padding: 0; box-sizing: border-box; }
  html, body { width: 800px; height: 1200px; overflow: hidden; background: var(--backdrop); }
  body { display: flex; align-items: center; justify-content: center; }
  .flyer {
    position: relative; width: 800px; height: 1035px; overflow: hidden;
    background: radial-gradient(ellipse at 50% 40%, var(--navy) 0%, var(--navy-deep) 100%);
    font-family: 'Roboto', Arial, sans-serif; color: var(--white);
  }
  .brand {
    position: absolute; top: 52px; left: 0; width: 800px;
    display: flex; justify-content: center; align-items: center; gap: 14px;
  }
  .brand-dot { width: 18px; height: 18px; border-radius: 50%; background: var(--green); }
  .brand-name {
    font-weight: 900; font-size: 58px; letter-spacing: 3px;
    color: var(--green); line-height: 1;
  }
  .package {
    position: absolute; top: 186px; width: 220px; height: 364px;
    border-radius: 0 44px 0 44px; font-family: 'Open Sans', Arial, sans-serif;
  }
  .package--horizon { left: 51px; background: linear-gradient(180deg, var(--green-dark), var(--green)); }
  .package--amber { left: 301px; background: linear-gradient(180deg, var(--grey-top), var(--grey-bottom)); }
  .package--evergreen { left: 546px; background: linear-gradient(180deg, var(--orange-top), var(--orange-bottom)); }
  .package-title {
    position: absolute; top: 30px; left: 20px;
    font-size: 16px; font-weight: 400;
  }
  .price-pill {
    position: absolute; top: 70px; left: 0; width: 154px; height: 64px;
    background: var(--white); border-radius: 0 32px 32px 0;
    font-family: 'Roboto', Arial, sans-serif; font-weight: 500;
    font-size: 32px; color: var(--price-grey); line-height: 64px; padding-left: 20px;
  }
  .features { position: absolute; top: 145px; left: 16px; list-style: none; font-size: 13px; }
  .features li { display: flex; align-items: center; gap: 8px; height: 26px; }
  .tick { width: 11px; height: 11px; flex: none; }
  .saving {
    position: absolute; top: 234px; left: 0; width: 100%; text-align: center;
    font-family: 'Roboto', Arial, sans-serif; font-weight: 700; font-size: 18px;
  }
  .buy-button {
    position: absolute; top: 279px; left: 23px; width: 175px; height: 33px;
    border: 1.5px solid var(--white); border-radius: 17px;
    font-family: 'Roboto', Arial, sans-serif; font-size: 11.5px;
    text-align: center; line-height: 30px;
  }
  .rewards { position: absolute; top: 582px; left: 0; width: 800px; text-align: center; }
  .rewards-main { font-size: 20px; line-height: 28px; color: var(--white); }
  .rewards-sub { font-size: 20px; line-height: 28px; color: var(--green); margin-top: 2px; }
  .dish { position: absolute; top: 650px; left: 0; width: 800px; height: 306px; }
  .footer-band {
    position: absolute; top: 956px; left: 0; width: 800px; height: 79px;
    background: var(--green); text-align: center;
  }
  .footer-note { margin-top: 13px; font-size: 14px; line-height: 18px; letter-spacing: 0.3px; }
  .footer-site { margin-top: 4px; font-size: 24px; line-height: 30px; font-weight: 700; }
  .footer-arrow { position: absolute; left: 198px; top: 20px; }
</style>
</head>
<body>
<main class="flyer">
  <header class="brand">
    <span class="brand-dot"></span>
    <span class="brand-name">BRAMBLEFORK</span>
  </header>

  <section class="package package--horizon">
    <h2 class="package-title">Horizon Package</h2>
    <div class="price-pill">$195</div>
    <ul class="features">
      <li><svg class="tick" viewBox="0 0 12 12"><circle cx="6" cy="6" r="6" fill="#fff"/><path d="M3.2 6.2 5.1 8 8.8 4.2" fill="none" stroke="#63ad3a" stroke-width="1.6"/></svg>1 week package (7 days )</li>
      <li><svg class="tick" viewBox="0 0 12 12"><circle cx="6" cy="6" r="6" fill="#fff"/><path d="M3.2 6.2 5.1 8 8.8 4.2" fill="none" stroke="#63ad3a" stroke-width="1.6"/></svg>2 meals a day</li>
    </ul>
    <div class="buy-button">BUY NOW</div>
  </section>

  <section class="package package--amber">
    <h2 class="package-title">Amber Package</h2>
    <div class="price-pill">$546</div>
    <ul class="features">
      <li><svg class="tick" viewBox="0 0 12 12"><circle cx="6" cy="6" r="6" fill="#fff"/><path d="M3.2 6.2 5.1 8 8.8 4.2" fill="none" stroke="#999" stroke-width="1.6"/></svg>3 week package (21 days)</li>
      <li><svg class="tick" viewBox="0 0 12 12"><circle cx="6" cy="6" r="6" fill="#fff"/><path d="M3.2 6.2 5.1 8 8.8 4.2" fill="none" stroke="#999" stroke-width="1.6"/></svg>2 meals per day</li>
    </ul>
    <p class="saving">Save $42.00!</p>
    <div class="buy-button">BUY NOW</div>
  </section>

  <section class="package package--evergreen">
    <h2 class="package-title">Evergreen Package</h2>
    <div class="price-pill">$1080</div>
    <ul class="features">
      <li><svg class="tick" viewBox="0 0 12 12"><circle cx="6" cy="6" r="6" fill="#fff"/><path d="M3.2 6.2 5.1 8 8.8 4.2" fill="none" stroke="#e98a20" stroke-width="1.6"/></svg>6 week+ package (45 days)</li>
      <li><svg class="tick" viewBox="0 0 12 12"><circle cx="6" cy="6" r="6" fill="#fff"/><path d="M3.2 6.2 5.1 8 8.8 4.2" fill="none" stroke="#e98a20" stroke-width="1.6"/></svg>2 meals per day</li>
    </ul>
    <p class="saving">Save $180!</p>
    <div class="buy-button">BUY NOW</div>
  </section>

  <div class="rewards">
    <p class="rewards-main">Use the value of your package toward take out or meal prep!</p>
    <p class="rewards-sub">Start earning your rewards now!</p>
  </div>

  <svg class="dish" viewBox="0 0 800 306" role="img" aria-label="Photo of a plated meal: seared salmon with greens, mashed potatoes and rice on a white plate">
    <defs>
      <linearGradient id="dish-tone" x1="0" y1="0" x2="1" y2="1">
        <stop offset="0" stop-color="#d9a04a"/>
        <stop offset="0.45" stop-color="#b86a2c"/>
        <stop offset="0.75" stop-color="#d8cfb8"/>
        <stop offset="1" stop-color="#f2f0ec"/>
      </linearGradient>
    </defs>
    <path d="M0 240 Q390 -180 800 185" fill="none" stroke="var(--green)" stroke-width="2.5"/>
    <path d="M0 252 Q390 -162 800 197 L800 306 L0 306 Z" fill="url(#dish-tone)"/>
  </svg>

  <footer class="footer-band">
    <svg class="footer-arrow" width="20" height="30" viewBox="0 0 22 34" aria-hidden="true">
      <path d="M18 3 C6 6 4 18 10 28 M6 25 L10 29 L13 24" fill="none" stroke="#fff" stroke-width="1.5"/>
    </svg>
    <p class="footer-note">YOU CAN FIND MORE INFO ON OUR WEBSITE</p>
    <p class="footer-site">WWW.BRAMBLEFORKMEALS.COM</p>
  </footer>
</main>
</body>
</html>
```